Tech Tradeshow Brochure Design Project

Our tech recruiting firm in NYC is looking for a modern new pamphlet for an upcoming tech trade show. We've been in business for 25 years, which is most likely how long its been since we ever updated our brochures. Regardless, we're busy placing programmers and software engineers and need a new brochure design, perhaps a creative one in the shape of our logo which is a power button. We're in the middle of updating and modernizing our look which you can reference in our logo and a screenshot of our re-skinned website homepage.

We'd like something that uses the blue and green colors and caters to both professionals looking for tech jobs as well as young programmers who want to work in a start up firm. The final design should communicate approachable, modern technology recruitment services.
Updates

Hi Designers,

Looking forward to seeing the great work coming soon! I wanted to provide an update regarding the pamphlet length. We'd like to see use of a fun, innovative shape (as opposed to a basic rectangular shape) and the content would end up being about 3-4 pages. Hope this clarifies and please see the attached files for the use of logos. Thank you!

Hi all,

Have attached a PDF of the brochure text & content, if you'd like to include it within the design. Thank you very much. 

Target Market(s)

Software engineers, clients from companies looking to place talent

Industry/Entity Type

Software

Requirements
Must have
• -Must have our logo and slogan: Powering tech careers for 25 years.
-Include the text of the PDF.
Nice to have
• Must utilize our colors and be visually stimulating

```html
<!DOCTYPE html>
<html lang="en">
<head>
<meta charset="utf-8">
<title>brightfield – Trade Show Brochure, Inside and Outside</title>
<link rel="stylesheet" href="https://fonts.googleapis.com/css2?family=Nunito:wght@700;800&family=Nunito+Sans:wght@300;400;600;700&display=swap">
<style>
  :root {
    --navy: #1c3563;
    --navy-deep: #172c55;
    --green: #9dbd5f;
    --green-text: #9cbc5c;
    --panel-grey: #dcdcdc;
    --sage: #98a48b;
    --sage-light: #a9b3a0;
    --white: #ffffff;
    --body-grey: #5a6275;
  }
  * { box-sizing: border-box; margin: 0; padding: 0; }
  html, body { width: 1200px; height: 927px; overflow: hidden; background: var(--white); }
  body { position: relative; font-family: "Nunito Sans", Arial, sans-serif; color: var(--navy); }
  .abs { position: absolute; }

  .spread-label {
    position: absolute; top: 18px; font-family: "Nunito", Arial, sans-serif;
    font-weight: 800; font-size: 38px; color: var(--navy-deep); line-height: 1;
  }

  /* ---------- inside ---------- */
  .inside { left: 13px; top: 66px; width: 578px; height: 815px; position: absolute; overflow: hidden; }
  .cover-brand { left: 0; top: 0; width: 267px; height: 271px; background: var(--panel-grey); }
  .brand-mark { position: absolute; border-radius: 50%; background: var(--navy); }
  .brand-name { position: absolute; font-weight: 400; color: var(--navy); line-height: 1; letter-spacing: 0.5px; }
  .slogan { position: absolute; font-size: 11px; color: var(--navy); line-height: 1; }

  .intro { left: 267px; top: 0; width: 311px; height: 271px; background: var(--navy); }
  .intro-tag { position: absolute; left: 83px; top: 42px; width: 228px; height: 53px; background: var(--panel-grey); }
  .intro-copy { position: absolute; left: 86px; top: 104px; width: 220px; color: var(--white);
    font-weight: 700; font-size: 8.6px; line-height: 18px; }
  .intro-copy .link { color: var(--green); }
  .intro-copy p + p { margin-top: 18px; }

  .services { left: 0; top: 271px; width: 578px; height: 271px; background: var(--panel-grey); }
  .art-languages { position: absolute; left: 18px; top: 8px; width: 190px; height: 258px;
    background: radial-gradient(circle at 50% 35%, #b9c3d6 0%, #cfd4dd 55%, var(--panel-grey) 80%); border-radius: 8px; }
  .tagline { position: absolute; left: 82px; top: 160px; font-size: 36px; font-weight: 400;
    color: var(--green-text); line-height: 37px; }
  .tagline span { display: block; }
  .tagline .second { margin-left: -24px; }
  .rule-v { position: absolute; width: 2px; background: var(--green); }
  .rule-h { position: absolute; height: 2px; background: var(--green); }
  .services-label { position: absolute; left: 323px; top: 183px; transform-origin: left top; transform: rotate(-90deg);
    font-family: "Nunito", Arial, sans-serif; font-weight: 800; font-size: 30px; color: var(--green-text); line-height: 1; white-space: nowrap; }
  .service { position: absolute; left: 369px; width: 200px; }
  .service h3 { font-weight: 400; font-size: 18.5px; color: var(--green-text); line-height: 22px; }
  .service p { font-size: 9.6px; line-height: 17px; color: var(--body-grey); margin-top: 2px; }

  .offer { left: 0; top: 542px; width: 578px; height: 273px; background: var(--green); }
  .offer-title { position: absolute; left: 0; width: 578px; top: 6px; text-align: center;
    font-family: "Nunito", Arial, sans-serif; font-weight: 800; font-size: 38px; color: var(--navy); line-height: 46px; letter-spacing: -0.3px; }
  .offer-divider { position: absolute; top: 52px; width: 2px; height: 221px; background: var(--navy); }
  .benefit { position: absolute; top: 64px; width: 160px; }
  .benefit h3 { font-family: "Nunito", Arial, sans-serif; font-weight: 700; font-size: 16.5px; line-height: 23px;
    color: var(--white); text-align: center; padding-bottom: 4px; border-bottom: 2px solid var(--navy); }
  .benefit p { font-size: 11.4px; line-height: 17.5px; color: var(--navy); margin-top: 14px; }

  /* ---------- outside ---------- */
  .outside { left: 613px; top: 66px; width: 578px; height: 815px; position: absolute; overflow: hidden; background: var(--navy); }
  .outside-top { left: 0; top: 0; width: 578px; height: 232px; background: var(--sage); }
  .outside-stripe { left: 0; top: 232px; width: 578px; height: 7px; background: var(--navy); }
  .outside-band { left: 0; top: 239px; width: 578px; height: 37px; background: var(--sage-light); }
</style>
</head>
<body>
  <div class="spread-label" style="left:207px;">Inside</div>
  <div class="spread-label" style="left:828px;">Outside</div>

  <section class="inside" aria-label="Brochure inside spread">
    <div class="abs cover-brand">
      <div class="brand-mark" style="left:77px; top:44px; width:114px; height:114px;"></div>
      <div class="brand-name" style="left:68px; top:212px; font-size:35px;">brightfield</div>
      <div class="slogan" style="left:72px; top:251px;">powering tech careers for 25 years</div>
    </div>

    <div class="abs intro">
      <div class="intro-tag">
        <div class="brand-mark" style="left:8px; top:8px; width:36px; height:36px;"></div>
        <div class="brand-name" style="left:52px; top:9px; font-size:26px;">brightfield</div>
        <div class="slogan" style="left:54px; top:38px; font-size:9.5px;">powering tech careers for 25 years</div>
      </div>
      <div class="intro-copy">
        <p>Brightfield's tech recruiters have not only established relationships with hiring decision makers of the most desired NYC firms today, but, we also have the inside scoop on important hiring trends going on now and what you need to know to compete in the future.</p>
        <p>for more info visit us at <span class="link">www.brightfield-talent.com</span></p>
      </div>
    </div>

    <div class="abs services">
      <div class="art-languages" role="img" aria-label="Illustration of a cheerful programmer with a speech bubble of linked circles naming programming languages"></div>
      <div class="rule-v" style="left:185px; top:0; height:44px;"></div>
      <div class="tagline"><span>we speak</span><span class="second">your language</span></div>
      <div class="services-label">our services</div>
      <div class="rule-v" style="left:356px; top:0; height:262px;"></div>

      <div class="service" style="top:18px;">
        <h3>Recruitment Services</h3>
        <p>Brightfield assists our clients with tech recruiting for both permanent and consulting services.</p>
      </div>
      <div class="rule-h" style="left:362px; top:97px; width:216px;"></div>
      <div class="service" style="top:100px;">
        <h3>Advisory Services</h3>
        <p>We provide a full range of advisory services which are available to our client companies.</p>
      </div>
      <div class="rule-h" style="left:362px; top:181px; width:216px;"></div>
      <div class="service" style="top:186px;">
        <h3>Interview Preparation</h3>
        <p>We offer candidates with as much information as possible so that they can be prepared for the interview process.</p>
      </div>
    </div>

    <div class="abs offer">
      <h2 class="offer-title">what we offer</h2>
      <div class="offer-divider" style="left:184px;"></div>
      <div class="offer-divider" style="left:396px;"></div>

      <div class="benefit" style="left:16px; width:160px;">
        <h3>Long-Standing Relationships</h3>
        <p>Brightfield has established long-standing relationships with our clients and have earned their trust.</p>
      </div>
      <div class="benefit" style="left:203px; width:160px;">
        <h3>No Commissioned Recruiters</h3>
        <p>Brightfield does not hire salespeople who compete for a commission.</p>
      </div>
      <div class="benefit" style="left:408px; width:162px;">
        <h3>No Voicemail-<br>People to People</h3>
        <p>When you call us you will not be subjected to voice-mail, you will always speak to a person.</p>
      </div>
    </div>
  </section>

  <section class="outside" aria-label="Brochure outside cover">
    <div class="abs outside-top">
      <div class="brand-mark" style="left:143px; top:92px; width:58px; height:58px;"></div>
      <div class="brand-name" style="left:220px; top:102px; font-size:42px;">brightfield</div>
      <div class="slogan" style="left:222px; top:148px; font-size:11px;">powering tech careers for 25 years</div>
    </div>
    <div class="abs outside-stripe"></div>
    <div class="abs outside-band"></div>
  </section>
</body>
</html>
```